Business Card Design Project

Recently had a new logo made up for my company and new business cards done as well. I have attached the logos for your viewing. Additional projects may be needed. Good luck!

Business

```html
<!DOCTYPE html>
<html lang="en">
<head>
<meta charset="utf-8">
<title>Marrow Financial Group – Business Cards</title>
<link href="https://fonts.googleapis.com/css2?family=Open+Sans:wght@400;600&display=swap" rel="stylesheet">
<style>
  :root {
    --bg: #d9d6d4;
    --card: #222224;
    --card-edge: #2c2c2f;
    --gold: #c6b27a;
    --white: #f2f2f2;
    --muted: #d8d8d8;
  }
  * { box-sizing: border-box; margin: 0; padding: 0; }
  html, body {
    width: 1200px; height: 960px; overflow: hidden;
    background: var(--bg);
    font-family: "Open Sans", Arial, sans-serif;
  }
  .canvas {
    position: relative; width: 1200px; height: 960px;
  }
  .card {
    position: absolute; left: 250px; width: 700px; height: 400px;
    background: linear-gradient(135deg, var(--card-edge), var(--card));
    box-shadow: 0 10px 24px rgba(0,0,0,.25);
  }
  .card-front { top: 40px; }
  .card-back { top: 520px; display: flex; align-items: center; justify-content: center; }

  /* front */
  .brand-block {
    position: absolute; left: 0; top: 0; width: 360px; height: 400px;
    display: flex; flex-direction: column; align-items: center; justify-content: center; gap: 26px;
  }
  .brand-square {
    width: 150px; height: 150px; border: 8px solid var(--gold);
  }
  .brand-name {
    color: var(--gold); font-weight: 600; text-transform: uppercase;
    text-align: center; font-size: 30px; letter-spacing: 4px; line-height: 1.25;
  }
  .divider {
    position: absolute; left: 372px; top: 40px; width: 2px; height: 320px;
    background: linear-gradient(to bottom, transparent, var(--gold) 20%, var(--gold) 80%, transparent);
  }
  .contact {
    position: absolute; left: 405px; top: 110px; color: var(--white);
  }
  .contact-name { font-size: 24px; font-weight: 600; }
  .contact-title { font-size: 13px; color: var(--muted); margin-top: 2px; }
  .contact-address { font-size: 14px; margin-top: 28px; line-height: 1.5; }
  .contact-list { list-style: none; margin-top: 4px; font-size: 14px; line-height: 1.6; }
  .contact-list li { display: flex; align-items: center; gap: 8px; }
  .contact-list svg { width: 12px; height: 12px; fill: var(--gold); flex: none; }

  /* back */
  .back-lockup { display: flex; align-items: center; gap: 18px; }
  .back-square { width: 80px; height: 80px; border: 5px solid var(--gold); }
  .back-name {
    color: var(--gold); font-weight: 600; text-transform: uppercase;
    font-size: 30px; letter-spacing: 5px;
  }
</style>
</head>
<body>
<main class="canvas">
  <section class="card card-front">
    <div class="brand-block">
      <div class="brand-square"></div>
      <div class="brand-name">Marrow<br>Financial Group</div>
    </div>
    <div class="divider"></div>
    <div class="contact">
      <div class="contact-name">Daniel R. Marrow</div>
      <div class="contact-title">Estate Planning and Insurance Specialist</div>
      <div class="contact-address">4120 Harbor Crest Road, Suite 310E<br>Brookfield, New York 11850</div>
      <ul class="contact-list">
        <li><svg viewBox="0 0 24 24"><path d="M6.6 10.8a15.1 15.1 0 006.6 6.6l2.2-2.2a1 1 0 011-.25 11.4 11.4 0 003.6.57 1 1 0 011 1V20a1 1 0 01-1 1A17 17 0 013 4a1 1 0 011-1h3.5a1 1 0 011 1 11.4 11.4 0 00.57 3.6 1 1 0 01-.25 1z"/></svg>555-218-4630</li>
        <li><svg viewBox="0 0 24 24"><path d="M6 2h12v6H6zM3 9h18a1 1 0 011 1v8h-4v4H6v-4H2v-8a1 1 0 011-1zm5 7v4h8v-4z"/></svg>555-218-4671</li>
        <li><svg viewBox="0 0 24 24"><path d="M2 5h20v14H2zm2 2v.5l8 5 8-5V7l-8 5z"/></svg>dmarrow@marrowfinancial.com</li>
        <li><svg viewBox="0 0 24 24"><path d="M12 2a10 10 0 100 20 10 10 0 000-20zm6.9 6h-3a15 15 0 00-1.3-3.9A8 8 0 0118.9 8zM12 4a13 13 0 011.8 4h-3.6A13 13 0 0112 4zM4.3 14a8 8 0 010-4h3.4a16 16 0 000 4zm.8 2h3a15 15 0 001.3 3.9A8 8 0 015.1 16zM8 8H5.1a8 8 0 014.3-3.9A15 15 0 008 8zm4 12a13 13 0 01-1.8-4h3.6A13 13 0 0112 20zm2.3-6H9.7a14 14 0 010-4h4.6a14 14 0 010 4zm.3 5.9A15 15 0 0016 16h3a8 8 0 01-4.4 3.9zM16.3 14a16 16 0 000-4h3.4a8 8 0 010 4z"/></svg>www.marrowfinancial.com</li>
      </ul>
    </div>
  </section>

  <section class="card card-back">
    <div class="back-lockup">
      <div class="back-square"></div>
      <div class="back-name">Marrow Financial Group</div>
    </div>
  </section>
</main>
</body>
</html>
```